Business Card Design

Divorce
Collaborative Family Law
Family Dispute Resolution
Family Law Property & Children

Target Market(s)

Australia

Industry/Entity Type

Business

Contact Information for Business Card

Delphine Hartwell
M App Law (Family Law) LLB (Hons) BA (Hons) Ass Dip Ag (HH)
Family Dispute Resolution Provider
Hartwell Family Law
PO Box 4723 Wrenfield 3806
Phone 03 58217000 Fax 03 58217100 Email hartwellfamilylaw@quillnet.example

Colors
f04a51

Requirements
Should not have
• Any reference to
United States or US terminology
the word Company

```html
<!DOCTYPE html>
<html lang="en">
<head>
<meta charset="utf-8">
<title>Hartwell Family Law – Business Card</title>
<link rel="stylesheet" href="https://fonts.googleapis.com/css2?family=Cinzel:wght@400;500&family=Lato:wght@400&display=swap">
<style>
  :root {
    --navy: #0e3858;
    --gold: #b8924a;
    --gold-light: #d4b070;
    --white: #ffffff;
    --backdrop: #e9e6e1;
  }
  * { margin: 0; padding: 0; box-sizing: border-box; }
  html, body {
    width: 1200px; height: 1024px; overflow: hidden;
    background: var(--backdrop);
  }
  .canvas { position: relative; width: 1200px; height: 1024px; }

  .card {
    position: absolute; left: 190px; width: 820px; height: 469px;
    box-shadow: 0 4px 14px rgba(0,0,0,0.18);
    overflow: hidden;
  }

  /* Front */
  .card-front { top: 30px; background: var(--white); }
  .front-stripe {
    position: absolute; top: 0; right: 52px; width: 70px; height: 100%;
    background: var(--navy);
  }
  .front-block {
    position: absolute; left: 0; top: 96px; width: 62px; height: 80px;
    background: var(--navy);
  }
  .front-accent {
    position: absolute; left: 76px; top: 100px; width: 6px; height: 72px;
    background: var(--gold);
  }
  .holder { position: absolute; left: 98px; top: 104px; }
  .holder-name {
    font-family: "Cinzel", serif; font-weight: 500;
    font-size: 30px; color: var(--navy); letter-spacing: 1px; line-height: 1.1;
  }
  .holder-role {
    font-family: "Lato", sans-serif; font-size: 19px; color: var(--gold);
    margin-top: 4px;
  }
  .contact-list {
    position: absolute; left: 300px; top: 292px; list-style: none;
  }
  .contact-list li {
    display: flex; align-items: center; gap: 12px; height: 30px;
    font-family: "Lato", sans-serif; font-size: 20px; color: var(--gold);
    white-space: nowrap;
  }
  .contact-key {
    flex: none;
    width: 20px; height: 20px; background: var(--navy); color: var(--white);
    font-size: 12px; display: flex; align-items: center; justify-content: center;
  }

  /* Back */
  .card-back { top: 529px; background: var(--navy); text-align: center; }
  .firm-name {
    margin-top: 128px;
    font-family: "Cinzel", serif; font-weight: 400;
    font-size: 58px; color: var(--gold); letter-spacing: 1px; line-height: 1;
  }
  .firm-rule { display: block; margin: 22px auto 22px; }
  .services {
    font-family: "Lato", sans-serif; font-size: 20px; color: var(--white);
    line-height: 1.6;
  }
</style>
</head>
<body>
<div class="canvas">

  <section class="card card-front" aria-label="Business card front">
    <div class="front-stripe"></div>
    <div class="front-block"></div>
    <div class="front-accent"></div>
    <div class="holder">
      <p class="holder-name">DELPHINE HARTWELL</p>
      <p class="holder-role">Advocate</p>
    </div>
    <ul class="contact-list">
      <li><span class="contact-key">P</span>03 58217000</li>
      <li><span class="contact-key">F</span>03 58217100</li>
      <li><span class="contact-key">E</span>hartwellfamilylaw@quillnet.example</li>
      <li><span class="contact-key">A</span>P.O. Box 4723 Wrenfield 3806</li>
    </ul>
  </section>

  <section class="card card-back" aria-label="Business card back">
    <h1 class="firm-name">HARTWELL FAMILY LAW</h1>
    <svg class="firm-rule" width="640" height="4" viewBox="0 0 640 4" aria-hidden="true">
      <defs>
        <linearGradient id="rule-fade" x1="0" x2="1" y1="0" y2="0">
          <stop offset="0" stop-color="#b8924a" stop-opacity="0.2"/>
          <stop offset="0.35" stop-color="#d4b070"/>
          <stop offset="0.7" stop-color="#b8924a"/>
          <stop offset="1" stop-color="#b8924a" stop-opacity="0"/>
        </linearGradient>
      </defs>
      <rect width="640" height="4" fill="url(#rule-fade)"/>
    </svg>
    <p class="services">Divorce | Collaborative Family Law | Family Dispute Resolution</p>
    <p class="services">Family Law Property &amp; Children</p>
  </section>

</div>
</body>
</html>
```